Gourmet butcher shop needs a business card design

We need a business card design for an upmarket butcher shop in Brisbane, Queensland Australia. We would prefer the card to be printed on a brown craft paper business card and would consider the use of raised print on the card. The card needs to make space for the usual information: ABN, address, telephone, facebook page. I stress it is a gourmet shop in a wealthy suburb. Thanks

Industry/Entity Type

Business

Contact Information for Business Card

Address Shop 7, Marrowbank Arcade, 417 Hollister Road, Ashcombe
Telephone 07 3581 4927
A.B.N. 53 874 910 326
Facebook www.facebook.com/quillbyprimecuts

Requirements
Should not have
• No need for a person's name or title

```html
<!DOCTYPE html>
<html lang="en">
<head>
<meta charset="utf-8">
<title>Quillby Prime Cuts – Business Card</title>
<link rel="stylesheet" href="https://fonts.googleapis.com/css2?family=Kanit:wght@400;500;600&family=Libre+Baskerville:ital@1&display=swap">
<style>
  :root {
    --page: #eeeeec;
    --kraft: #c9a67d;
    --kraft-deep: #bc966a;
    --ink: #2b2a2e;
    --red: #d3323b;
  }
  * { box-sizing: border-box; margin: 0; padding: 0; }
  html, body { width: 1200px; height: 800px; overflow: hidden; background: var(--page); }
  .canvas {
    width: 1200px; height: 800px;
    display: flex; align-items: center; justify-content: center; gap: 40px;
  }
  .card {
    position: relative; width: 540px; height: 320px; overflow: hidden;
    background: radial-gradient(circle at 30% 30%, var(--kraft), var(--kraft-deep));
    font-family: "Kanit", sans-serif; color: var(--ink);
  }
  .card__frame-outer { position: absolute; inset: 9px; border: 3px solid var(--ink); }
  .card__frame-inner { position: absolute; inset: 17px; border: 2px solid var(--red); }

  /* brand lockup */
  .brand { position: absolute; text-align: center; }
  .brand__tagline {
    font-family: "Libre Baskerville", serif; font-style: italic; white-space: nowrap;
    display: flex; align-items: center; gap: 8px; justify-content: center;
  }
  .brand__tagline::before, .brand__tagline::after,
  .brand__rule { content: ""; display: block; height: 1px; background: var(--ink); flex: 1; }
  .brand__name { font-weight: 600; color: var(--red); text-transform: uppercase; line-height: 1.02; white-space: nowrap; }

  /* contact side */
  .contact { position: absolute; left: 34px; top: 90px; }
  .contact__abn {
    font-weight: 500; font-size: 15px; letter-spacing: 0.5px; white-space: nowrap;
    display: inline-block; padding-bottom: 2px; border-bottom: 2px solid var(--red);
    margin-bottom: 20px;
  }
  .contact__list { list-style: none; }
  .contact__item {
    display: flex; align-items: flex-start; gap: 10px; white-space: nowrap;
    font-weight: 500; font-size: 14.5px; line-height: 1.4; margin-bottom: 6px;
  }
  .contact__icon {
    flex: none; width: 22px; height: 20px;
    border-right: 1.5px solid var(--red); border-bottom: 1.5px solid var(--red);
    display: flex; align-items: center; justify-content: center;
  }
  .contact__icon svg { width: 13px; height: 13px; }
  .contact__square { width: 9px; height: 9px; background: var(--red); }

  .card--contact .brand { right: 44px; top: 102px; width: 216px; }
  .card--contact .brand__tagline { font-size: 9px; margin-bottom: 4px; }
  .card--contact .brand__name { font-size: 29px; }
  .card--contact .brand__rule { margin-top: 8px; }

  .card--brand .brand { left: 60px; right: 60px; top: 76px; }
  .card--brand .brand__tagline { font-size: 14px; margin-bottom: 10px; }
  .card--brand .brand__name { font-size: 62px; }
  .card--brand .brand__rule { margin-top: 16px; }
</style>
</head>
<body>
<main class="canvas">
  <section class="card card--brand">
    <div class="card__frame-outer"></div>
    <div class="card__frame-inner"></div>
    <div class="brand">
      <p class="brand__tagline">Simply cut finer</p>
      <h1 class="brand__name">Quillby<br>Prime Cuts</h1>
      <span class="brand__rule"></span>
    </div>
  </section>

  <section class="card card--contact">
    <div class="card__frame-outer"></div>
    <div class="card__frame-inner"></div>
    <div class="contact">
      <p class="contact__abn">A.B.N. 53 874 910 326</p>
      <ul class="contact__list">
        <li class="contact__item">
          <span class="contact__icon"><svg viewBox="0 0 24 24"><path fill="none" stroke="#d3323b" stroke-width="2.2" d="M6 3h4l2 5-3 2a11 11 0 0 0 5 5l2-3 5 2v4a2 2 0 0 1-2 2A17 17 0 0 1 4 5a2 2 0 0 1 2-2z"/></svg></span>
          07 3581 4927
        </li>
        <li class="contact__item">
          <span class="contact__icon"><span class="contact__square"></span></span>
          quillbyprimecuts
        </li>
        <li class="contact__item">
          <span class="contact__icon"><svg viewBox="0 0 24 24"><path fill="#d3323b" d="M12 2a7 7 0 0 0-7 7c0 5 7 13 7 13s7-8 7-13a7 7 0 0 0-7-7zm0 9.5A2.5 2.5 0 1 1 12 6.5a2.5 2.5 0 0 1 0 5z"/></svg></span>
          <span>Shop 7. Marrowbank Arcade,<br>417 Hollister Road,<br>Ashcombe</span>
        </li>
      </ul>
    </div>
    <div class="brand">
      <p class="brand__tagline">Simply cut finer</p>
      <p class="brand__name">Quillby<br>Prime Cuts</p>
      <span class="brand__rule"></span>
    </div>
  </section>
</main>
</body>
</html>
```